Two Bodyguards

Cover for a book in French language:
- Author: Mathieu Ferrand-Lacoste
- Title: Cold suspects rarely ever smile back
- Publisher (at the bottom of the page): Editions Vernaille
Key Words:
- a rich man died recently, it looks like a murder. He has been found in his luxury apartment.
- Two Body Guards: one is elegant, the other a bit fat.
- two pretty women.
- Inheritance (wealth)
Size of the cover: 14 x 20.5 cm (+ bleed area)
Please note that the title should remain in English: "Suspects rarely ever smile back".
By the way the title doesn't mean anything. It's just a joke.
Thrillers' reader

```html
<!DOCTYPE html>
<html lang="en">
<head>
<meta charset="utf-8">
<title>Cold suspects rarely ever smile back — Book Cover</title>
<link rel="stylesheet" href="https://fonts.googleapis.com/css2?family=Cinzel:wght@400&family=Lato:wght@400&display=swap">
<style>
  :root {
    --stage: #000000;
    --paper-light: #f5f5f5;
    --paper-mid: #d6d6d6;
    --ink: #151515;
    --shadow-black: #060606;
    --shadow-deep: #120304;
    --rim-red: #9a1016;
    --title-white: #ffffff;
  }
  * { margin: 0; padding: 0; box-sizing: border-box; }
  html, body {
    width: 1200px;
    height: 926px;
    overflow: hidden;
    background: var(--stage);
  }
  .book-cover {
    position: absolute;
    left: 346px;
    top: 62px;
    width: 508px;
    height: 814px;
    overflow: hidden;
    background: radial-gradient(ellipse at 50% 30%, var(--paper-light) 0%, var(--paper-light) 40%, var(--paper-mid) 100%);
  }
  .author-name {
    position: absolute;
    top: 34px;
    left: 0;
    width: 100%;
    text-align: center;
    font-family: "Cinzel", serif;
    font-size: 25px;
    letter-spacing: 3.5px;
    color: var(--ink);
  }
  .bodyguards-art {
    position: absolute;
    left: 42px;
    top: 78px;
    width: 424px;
    height: 736px;
  }
  .figure-block {
    position: absolute;
    bottom: 0;
    background: linear-gradient(to right, var(--shadow-deep) 0%, var(--shadow-black) 18%, var(--shadow-black) 82%, var(--shadow-deep) 100%);
    box-shadow: 0 0 16px rgba(154, 16, 20, 0.6), inset 0 0 10px rgba(154, 16, 20, 0.45);
  }
  .figure-block--heavy {
    left: 0;
    width: 206px;
    top: 0;
    border-radius: 90px 70px 0 0;
  }
  .figure-block--elegant {
    left: 210px;
    width: 214px;
    top: 2px;
    border-radius: 70px 90px 0 0;
  }
  .ground-band {
    position: absolute;
    left: 0;
    bottom: 0;
    width: 100%;
    height: 96px;
    background: linear-gradient(to bottom, rgba(6,6,6,0) 0%, var(--shadow-black) 14px, var(--shadow-black) 100%);
  }
  .book-title {
    position: absolute;
    top: 232px;
    left: 0;
    width: 100%;
    text-align: center;
    font-family: "Cinzel", serif;
    font-weight: 400;
    color: var(--title-white);
    line-height: 1;
  }
  .book-title span { display: block; }
  .title-line-lead { font-size: 96px; }
  .title-line-main { font-size: 76px; margin-top: 6px; }
  .title-line-small { font-size: 36px; margin-top: 6px; }
  .title-line-close { font-size: 56px; margin-top: 0; }
  .publisher-name {
    position: absolute;
    bottom: 30px;
    left: 0;
    width: 100%;
    text-align: center;
    font-family: "Lato", sans-serif;
    font-size: 26px;
    color: var(--title-white);
  }
</style>
</head>
<body>
  <div class="book-cover">
    <div class="author-name">Mathieu Ferrand-Lacoste</div>
    <div class="bodyguards-art" role="img" aria-label="Backlit silhouettes of two bodyguards standing side by side, one heavy-set in a coat, one elegant in a suit holding a rifle, rimmed with red light">
      <div class="figure-block figure-block--heavy"></div>
      <div class="figure-block figure-block--elegant"></div>
    </div>
    <div class="ground-band"></div>
    <h1 class="book-title">
      <span class="title-line-lead">COLD</span>
      <span class="title-line-main">SUSPECTS</span>
      <span class="title-line-small">RARELY EVER</span>
      <span class="title-line-close">SMILE BACK</span>
    </h1>
    <div class="publisher-name">Editions Vernaille</div>
  </div>
</body>
</html>
```